Business Card Design

I want a non fussy clear design. I like Vintage, Retro writing for the main name as it will be a banner for the roof sign.
Company name, address and ph no. I would also like a unisex symbol small in the corner of the card. The colour of the card does not have to be blue. But I do want a bright clean clear card. A head sillohette small in the other corner possibly.

Industry/Entity Type

Business

Contact Information for Business Card

Zet Hair Design
318 Kellaby Road, Kellaby
Ph (09) 4162903

Requirements
Must have
• The back of the card must have appointment time, date dont worry about the location as its obviously on the front of the card

```html
<!DOCTYPE html>
<html lang="en">
<head>
<meta charset="utf-8">
<title>Zet Hair Design – Business Card</title>
<link rel="stylesheet" href="https://fonts.googleapis.com/css2?family=Arimo:wght@400;700&family=Questrial&family=Lilita+One&display=swap">
<style>
  :root {
    --paper: #ffffff;
    --mint-light: #f4faec;
    --mint-edge: #c3e19c;
    --salon-green: #00923f;
    --name-red: #e8151d;
    --ink: #1a1a1a;
    --crop: #3a3a3a;
  }
  * { margin: 0; padding: 0; box-sizing: border-box; }
  html, body {
    width: 1200px; height: 383px; overflow: hidden;
    background: var(--paper);
  }
  .sheet { position: relative; width: 1200px; height: 383px; }

  .crop-marks { position: absolute; inset: 0; }

  .card-front {
    position: absolute; left: 31px; top: 30px; width: 570px; height: 325px;
    background: radial-gradient(ellipse 60% 70% at 50% 48%, var(--mint-light) 0%, #e3f1d0 55%, var(--mint-edge) 100%);
    overflow: hidden;
  }
  .corner-badge {
    position: absolute; top: 25px; width: 66px; height: 66px;
    border-radius: 50%; background: var(--salon-green);
  }
  .corner-badge--unisex { left: 25px; }
  .corner-badge--head { right: 24px; }

  .business-name {
    position: absolute; left: 0; right: 0; top: 122px;
    text-align: center;
    font-family: "Lilita One", sans-serif;
    font-size: 52px; color: var(--name-red);
    letter-spacing: 0.5px;
  }

  .address-band {
    position: absolute; left: 0; right: 0; bottom: 0; height: 62px;
    background: var(--salon-green);
    display: flex; align-items: center; justify-content: center;
    font-family: "Questrial", sans-serif; font-size: 18px;
    color: var(--paper); letter-spacing: 0.6px;
  }

  .card-back {
    position: absolute; left: 601px; top: 30px; width: 569px; height: 325px;
    background: var(--paper);
    font-family: "Arimo", sans-serif; color: var(--ink);
  }
  .appointment-title {
    position: absolute; left: 0; right: 0; top: 120px;
    text-align: center; font-weight: 700; font-size: 21px; letter-spacing: 0.3px;
  }
  .appointment-fields {
    position: absolute; left: 73px; top: 184px;
    display: flex; align-items: flex-end; font-size: 16px;
  }
  .field-line {
    display: inline-block; width: 162px; height: 1px;
    background: var(--ink); margin: 0 8px 3px 4px;
  }
</style>
</head>
<body>
<div class="sheet">
  <svg class="crop-marks" width="1200" height="383" viewBox="0 0 1200 383" aria-hidden="true">
    <g stroke="var(--crop)" stroke-width="1">
      <line x1="31.5" y1="0" x2="31.5" y2="18"/>
      <line x1="600.5" y1="0" x2="600.5" y2="18"/>
      <line x1="1170.5" y1="0" x2="1170.5" y2="18"/>
      <line x1="31.5" y1="365" x2="31.5" y2="383"/>
      <line x1="600.5" y1="365" x2="600.5" y2="383"/>
      <line x1="1170.5" y1="365" x2="1170.5" y2="383"/>
      <line x1="0" y1="30.5" x2="19" y2="30.5"/>
      <line x1="0" y1="355.5" x2="19" y2="355.5"/>
      <line x1="1182" y1="30.5" x2="1200" y2="30.5"/>
      <line x1="1182" y1="355.5" x2="1200" y2="355.5"/>
    </g>
  </svg>

  <section class="card-front">
    <div class="corner-badge corner-badge--unisex" role="img" aria-label="Unisex man and woman symbol"></div>
    <div class="corner-badge corner-badge--head" role="img" aria-label="Head silhouette in profile"></div>
    <h1 class="business-name">Zet Hair Design</h1>
    <p class="address-band">318 Kellaby Road, Kellaby. Ph (09) 4162903</p>
  </section>

  <section class="card-back">
    <h2 class="appointment-title">APPOINTMENT</h2>
    <p class="appointment-fields">
      <span>Time:</span><span class="field-line"></span>
      <span>Date:</span><span class="field-line"></span>
    </p>
  </section>
</div>
</body>
</html>
```